Northbrook Vertebral Clinic of Weldon
Spine Surgeon
Professional
Grant Pellow, DO
Board Certified, Fellowship Trained, Reconstructive and Minimally Invasive Spine Surgery
5183 W. Tamsworth Rd., Suite 204
Harlow, TX 75281
unknown at this time
unknown
grantjpellow@mailvex.net
www.NorthbrookVertebralClinic.net
Board Certified, Orthopedic surgery
Fellowship Trained, Reconstructive and Minimally Invasive Spine Surgery
Clearly highlight that I am board certified and fellowship trained in spine surgery.
I am setting up a new office and do not have phone lines ect. I will be changing my email address to a business account
Treatment of:
Back and Neck Pain,
Arm and Leg Pain,
Degenerative Disc Disease of the Spine,
Spinal Stenosis,
Herniated Discs,
Scoliosis and Spinal Deformities,
Spinal Tumors and Infections,
Spinal Compression Fractures,
Worker's Compensation Injuries,
Motor Vehicle Injuries

```html
<!DOCTYPE html>
<html lang="en">
<head>
<meta charset="utf-8">
<title>Northbrook Vertebral Clinic of Weldon – Stationery</title>
<link href="https://fonts.googleapis.com/css2?family=Cormorant+Garamond:wght@600&family=Open+Sans:wght@400;600&display=swap" rel="stylesheet">
<style>
:root{
  --bg:#e4e6e9;
  --paper:#ffffff;
  --blue:#1f5298;
  --blue-dark:#123a73;
  --blue-light:#3d74bd;
  --ink:#4a4f57;
  --muted:#8a9099;
  --faint:#eef0f3;
}
*{box-sizing:border-box;margin:0;padding:0}
html,body{width:1200px;height:871px;overflow:hidden}
body{background:var(--bg);position:relative;font-family:"Open Sans",sans-serif;color:var(--ink)}
.piece{position:absolute;background:var(--paper);box-shadow:0 3px 12px rgba(0,0,0,.18);overflow:hidden}
.brand{display:flex;align-items:center;gap:7px}
.brand-dot{width:22px;height:22px;border-radius:50%;background:var(--blue);flex:none}
.brand-name{font-family:"Cormorant Garamond",serif;font-weight:600;color:var(--blue);text-transform:uppercase;font-size:11px;line-height:1.1;letter-spacing:.04em;width:130px}
.watermark{position:absolute;border-radius:50%;background:var(--faint)}
.small{font-size:6.5px;line-height:1.5;color:var(--muted)}
.footer-bar{position:absolute;left:0;right:0;bottom:0;height:6px;background:linear-gradient(90deg,var(--blue-dark),var(--blue-light))}

/* letterhead */
.letterhead{left:40px;top:40px;width:300px;height:424px}
.letterhead .brand{position:absolute;left:22px;top:30px}
.letterhead .watermark{width:240px;height:240px;right:-70px;top:-40px}
.letterhead .footer{position:absolute;left:22px;right:22px;bottom:16px;border-top:1px solid #d6dae0;padding-top:5px;display:flex;flex-direction:column}

/* letter */
.letter{left:360px;top:40px;width:300px;height:424px}
.letter .brand{position:absolute;left:22px;top:30px}
.letter .body{position:absolute;left:22px;right:30px;top:110px;font-size:7px;line-height:1.7;color:var(--ink)}
.letter .body p{margin-bottom:8px}
.letter .sign{margin-top:16px}
.letter .footer{position:absolute;left:22px;right:22px;bottom:16px;border-top:1px solid #d6dae0;padding-top:5px;display:flex;flex-direction:column}

/* compliments slip */
.slip{left:690px;top:40px;width:470px;height:210px}
.slip .watermark{width:220px;height:220px;right:-40px;top:-60px}
.slip .brand{position:absolute;left:24px;top:24px}
.slip .title{position:absolute;right:28px;bottom:48px;font-family:"Cormorant Garamond",serif;font-weight:600;font-size:22px;color:var(--blue);text-transform:uppercase;letter-spacing:.08em}
.slip .contact{position:absolute;right:28px;top:24px;text-align:right}
.slip .contact strong{display:block;color:var(--blue);font-size:8px;font-weight:600}
.slip .footer{position:absolute;left:24px;right:24px;bottom:14px;text-align:center}

/* envelope */
.envelope{left:690px;top:274px;width:470px;height:210px}
.envelope .watermark{width:200px;height:200px;right:-30px;top:-50px}
.envelope .brand{position:absolute;left:24px;top:22px}
.envelope .return{position:absolute;left:24px;top:72px}
.envelope .band{position:absolute;left:0;right:0;bottom:0;height:34px;background:linear-gradient(90deg,var(--blue-dark),var(--blue-light))}

/* business cards */
.card{width:252px;height:144px}
.card-front{left:40px;top:500px;background:linear-gradient(135deg,var(--blue-light),var(--blue-dark))}
.card-front .brand-dot{background:#fff}
.card-front .brand-name{color:#fff}
.card-front .brand{position:absolute;left:20px;top:56px}
.card-back{left:40px;top:666px}
.card-back .brand{position:absolute;left:16px;top:16px}
.card-back .brand-name{width:100px;font-size:9px}
.card-back .person{position:absolute;right:16px;top:16px;text-align:right}
.card-back .person strong{display:block;font-size:9px;color:var(--blue);font-weight:600}
.card-back .details{position:absolute;left:16px;right:16px;bottom:16px}

/* CD */
.disc{position:absolute;left:330px;top:510px;width:320px;height:320px;border-radius:50%;
  background:radial-gradient(circle at 35% 30%,var(--blue-light),var(--blue) 55%,var(--blue-dark));box-shadow:0 3px 12px rgba(0,0,0,.25)}
.disc .hub{position:absolute;left:110px;top:110px;width:100px;height:100px;border-radius:50%;background:#f3f4f6;border:10px solid #d9dde3}
.disc .hole{position:absolute;left:30px;top:30px;width:20px;height:20px;border-radius:50%;background:var(--bg)}
.disc .brand{position:absolute;left:50%;top:52px;transform:translateX(-50%)}
.disc .brand-dot{background:#fff}
.disc .brand-name{color:#fff;width:130px}
.disc .url{position:absolute;left:0;right:0;bottom:44px;text-align:center;color:#dbe6f5;font-size:7px}

/* envelope back */
.env-back{left:690px;top:510px;width:470px;height:320px;background:var(--paper)}
.env-back svg{position:absolute;left:0;top:0}
.env-back .brand{position:absolute;left:50%;top:128px;transform:translateX(-50%)}
.env-back .brand-dot{background:#fff}
.env-back .brand-name{color:#fff;text-align:left}
</style>
</head>
<body>

<section class="piece letterhead" aria-label="Letterhead">
  <div class="watermark"></div>
  <div class="brand"><span class="brand-dot"></span><span class="brand-name">Northbrook Vertebral Clinic of Weldon</span></div>
  <div class="footer small"><span>5183 W. Tamsworth Rd., Suite 204 · Harlow, TX 75281</span><span>www.NorthbrookVertebralClinic.net</span></div>
  <div class="footer-bar"></div>
</section>

<section class="piece letter" aria-label="Letter">
  <div class="brand"><span class="brand-dot"></span><span class="brand-name">Northbrook Vertebral Clinic of Weldon</span></div>
  <div class="body">
    <p>Dear Patient, thank you for choosing our clinic for your spine care.</p>
    <p>Our team provides board certified and fellowship trained care for back and neck pain, disc disease, stenosis and spinal deformity.</p>
    <p>Please contact our office with any questions about your treatment plan.</p>
    <p class="sign">Sincerely,<br><strong>Grant Pellow, DO</strong></p>
  </div>
  <div class="footer small"><span>5183 W. Tamsworth Rd., Suite 204 · Harlow, TX 75281</span><span>www.NorthbrookVertebralClinic.net</span></div>
  <div class="footer-bar"></div>
</section>

<section class="piece slip" aria-label="Compliments slip">
  <div class="watermark"></div>
  <div class="brand"><span class="brand-dot"></span><span class="brand-name">Northbrook Vertebral Clinic of Weldon</span></div>
  <div class="contact small"><strong>Grant Pellow, DO</strong>Board Certified, Orthopedic Surgery<br>Fellowship Trained, Spine Surgery</div>
  <div class="title">With Compliments</div>
  <div class="footer small">5183 W. Tamsworth Rd., Suite 204 · Harlow, TX 75281 · grantjpellow@mailvex.net · www.NorthbrookVertebralClinic.net</div>
  <div class="footer-bar"></div>
</section>

<section class="piece envelope" aria-label="Envelope front">
  <div class="watermark"></div>
  <div class="brand"><span class="brand-dot"></span><span class="brand-name">Northbrook Vertebral Clinic of Weldon</span></div>
  <div class="return small">5183 W. Tamsworth Rd., Suite 204<br>Harlow, TX 75281</div>
  <div class="band"></div>
</section>

<section class="piece card card-front" aria-label="Business card front">
  <div class="brand"><span class="brand-dot"></span><span class="brand-name">Northbrook Vertebral Clinic of Weldon</span></div>
</section>

<section class="piece card card-back" aria-label="Business card back">
  <div class="brand"><span class="brand-dot"></span><span class="brand-name">Northbrook Vertebral Clinic of Weldon</span></div>
  <div class="person small"><strong>Grant Pellow, DO</strong>Board Certified<br>Fellowship Trained</div>
  <div class="details small">5183 W. Tamsworth Rd., Suite 204, Harlow, TX 75281<br>grantjpellow@mailvex.net<br>www.NorthbrookVertebralClinic.net</div>
  <div class="footer-bar"></div>
</section>

<section class="disc" aria-label="CD label">
  <div class="hub"><div class="hole"></div></div>
  <div class="brand"><span class="brand-dot"></span><span class="brand-name">Northbrook Vertebral Clinic of Weldon</span></div>
  <div class="url">5183 W. Tamsworth Rd., Suite 204 · Harlow, TX 75281<br>www.NorthbrookVertebralClinic.net</div>
</section>

<section class="piece env-back" aria-label="Envelope back">
  <svg width="470" height="320" viewBox="0 0 470 320">
    <defs>
      <linearGradient id="flap" x1="0" y1="0" x2="1" y2="1">
        <stop offset="0" stop-color="#3d74bd"/><stop offset="1" stop-color="#123a73"/>
      </linearGradient>
    </defs>
    <path d="M0 320 L235 170 L470 320 Z" fill="#f1f3f6"/>
    <path d="M0 0 L0 320 L200 180 Z" fill="#f7f8fa"/>
    <path d="M470 0 L470 320 L270 180 Z" fill="#f7f8fa"/>
    <path d="M0 0 H470 L250 205 Q235 216 220 205 Z" fill="url(#flap)"/>
  </svg>
  <div class="brand"><span class="brand-dot"></span><span class="brand-name">Northbrook Vertebral Clinic of Weldon</span></div>
</section>

</body>
</html>
```